Anzeigengestaltung für Zahnarztpraxis
Zielgruppe
Zahnarztpraxis
Aufgabenstellung
Möchte eine moderne Stellenanzeige, ggf. einen zum Logo farblich passenden Rahmen; ggf. noch mit Bildern

```html
<!DOCTYPE html>
<html lang="de">
<head>
<meta charset="utf-8">
<title>Stellenanzeige – Zahnarztpraxis Kochertal</title>
<link rel="stylesheet" href="https://fonts.googleapis.com/css2?family=EB+Garamond:wght@400;600;700&display=swap">
<style>
  :root {
    --paper: #ffffff;
    --ink: #111111;
    --edge: #b9b9b9;
    --brand: #2a5a8c;
  }
  * { margin: 0; padding: 0; box-sizing: border-box; }
  html, body { width: 989px; height: 1200px; overflow: hidden; background: var(--paper); }
  body { font-family: "EB Garamond", Georgia, serif; color: var(--ink); line-height: 1.2; }
  .ad {
    position: relative; width: 989px; height: 1200px;
    border-left: 1px solid var(--edge); border-right: 1px solid var(--edge);
  }
  .ad > * { position: absolute; }
  .headline { left: 100px; top: 24px; font-size: 52px; font-weight: 400; white-space: nowrap; }
  .brand { left: 528px; top: 12px; display: flex; align-items: center; gap: 18px; }
  .brand-dot { width: 96px; height: 96px; border-radius: 50%; background: var(--brand); }
  .brand-name { color: var(--brand); font-size: 36px; font-weight: 600; line-height: 1.05; }
  .center { left: 0; right: 0; text-align: center; white-space: nowrap; }
  .intro { top: 142px; font-size: 33px; }
  .job { font-size: 30px; font-weight: 700; letter-spacing: -0.3px; }
  .job-1 { top: 239px; }
  .job-2 { top: 287px; }
  .job .tag { margin-left: 30px; }
  .section-title { left: 0; font-size: 28px; }
  .benefits-title { top: 375px; }
  .values-title { top: 745px; }
  .checklist { list-style: none; font-size: 28px; white-space: nowrap; }
  .checklist li { display: flex; align-items: center; gap: 16px; height: 41px; }
  .checklist svg { width: 18px; height: 18px; flex: none; }
  .benefits { left: 40px; top: 419px; }
  .values { left: 48px; top: 791px; }
  .values strong { font-weight: 700; }
  .cta-title { top: 1004px; font-size: 32px; }
  .cta-line { font-size: 33px; }
  .cta-1 { top: 1048px; }
  .cta-2 { top: 1094px; }
  .cta-3 { top: 1140px; }
  .cta-line strong { font-weight: 700; margin-left: 8px; }
</style>
</head>
<body>
<main class="ad">
  <h1 class="headline">Komm ins Team der</h1>
  <div class="brand">
    <span class="brand-dot"></span>
    <span class="brand-name">Zahnarztpraxis<br>Kochertal</span>
  </div>

  <p class="center intro">Wir suchen in Vollzeit</p>
  <h2 class="center job job-1">Zahnmedizinische Fachangestellte <span class="tag">(m/w/d)</span></h2>
  <h2 class="center job job-2">Zahnmedizinische Prophylaxeassistent <span class="tag">(m/w/d)</span></h2>

  <p class="section-title benefits-title">Deine Vorteile:</p>
  <ul class="checklist benefits">
    <li><svg viewBox="0 0 16 16"><path d="M2 8.5l4 4L14 3" fill="none" stroke="#111" stroke-width="1.6"/></svg>Geregelte Arbeitszeiten</li>
    <li><svg viewBox="0 0 16 16"><path d="M2 8.5l4 4L14 3" fill="none" stroke="#111" stroke-width="1.6"/></svg>Top moderne Ausstattung</li>
    <li><svg viewBox="0 0 16 16"><path d="M2 8.5l4 4L14 3" fill="none" stroke="#111" stroke-width="1.6"/></svg>Spannende Mitarbeiterevents und Spaß bei der Arbeit</li>
    <li><svg viewBox="0 0 16 16"><path d="M2 8.5l4 4L14 3" fill="none" stroke="#111" stroke-width="1.6"/></svg>Etabliertes Qualitätsmanagement und klare Strukturen</li>
    <li><svg viewBox="0 0 16 16"><path d="M2 8.5l4 4L14 3" fill="none" stroke="#111" stroke-width="1.6"/></svg>Flexible Urlaubsplanung</li>
    <li><svg viewBox="0 0 16 16"><path d="M2 8.5l4 4L14 3" fill="none" stroke="#111" stroke-width="1.6"/></svg>Überdurchschnittliches Gehalt</li>
    <li><svg viewBox="0 0 16 16"><path d="M2 8.5l4 4L14 3" fill="none" stroke="#111" stroke-width="1.6"/></svg>Kostenfreie Zahnbehandlungen inkl. Bleaching</li>
  </ul>

  <p class="section-title values-title">Was uns wichtig ist:</p>
  <ul class="checklist values">
    <li><svg viewBox="0 0 16 16"><path d="M2 8.5l4 4L14 3" fill="none" stroke="#111" stroke-width="1.6"/></svg>Du bist aufgeschlossen und motiviert</li>
    <li><svg viewBox="0 0 16 16"><path d="M2 8.5l4 4L14 3" fill="none" stroke="#111" stroke-width="1.6"/></svg>Du bist kommunikativ und kontaktfreudig im Umgang mit Menschen</li>
    <li><svg viewBox="0 0 16 16"><path d="M2 8.5l4 4L14 3" fill="none" stroke="#111" stroke-width="1.6"/></svg>Du hast Freude an Deiner Arbeit</li>
    <li><svg viewBox="0 0 16 16"><path d="M2 8.5l4 4L14 3" fill="none" stroke="#111" stroke-width="1.6"/></svg><span>Dann bist <strong>DU</strong> die Verstärkung, die wir suchen!</span></li>
  </ul>

  <p class="center cta-title">Interesse?</p>
  <p class="center cta-line cta-1">Wir freuen uns über eine schriftliche Bewerbung</p>
  <p class="center cta-line cta-2">per Post an: <strong>Dr. Harbeck, Lindenstr. 12, 73980 Lindenau</strong></p>
  <p class="center cta-line cta-3">oder per Mail an: <strong>timo-harbeck@postfeld.de</strong></p>
</main>
</body>
</html>
```